GLP letterhead

We need a letterhead design for our new company based in Los Angeles called "Gold Lantern Pictures". We develop film and television projects. We work with investors, financiers, film production companies, film distribution and sales companies as well as studios. We would like to incorporate our logo (see attached) but make the letterhead simple and elegant. We need to include: logo, company address, phone number and company website.
Updates

Hello designers, Thanks for your submissions. For our letterhead, we are looking for something more simple and elegant. No heavy bars or lines. Make it feel light and clean. Not a lot of ink on the page. Use the logo and contact info but think "clean", "streamlined" and mostly white paper. Looking forward to seeing more... thanks! Gold Lantern Pictures team

Target Market(s)

Studio executives, talent agents and agencies, financiers, investors.

Industry/Entity Type

It Company

Requirements
Must have
• Gold Lantern Pictures logo (see attached). Logo may be cropped and altered appropriately for elegant letterhead design.
• Please include:
• COMPANY ADDRESS:
• Ridgeway Studio Park
• 2850 Halverson Street
• Tower Annex, 4th Floor
• Manhattan Beach, CA 90412
• COMPANY WEBSITE:
• www.goldlanternpicturesco.example
• COMPANY PHONE NUMBER:
• 310-555-0148

```html
<!DOCTYPE html>
<html lang="en">
<head>
<meta charset="utf-8">
<title>Gold Lantern Pictures — Letterhead</title>
<link rel="stylesheet" href="https://fonts.googleapis.com/css2?family=Dosis:wght@400;500;600&display=swap">
<style>
  :root {
    --paper: #ffffff;
    --backdrop: #ffffff;
    --rule: #1c5f6e;
    --rule-soft: #9cc8d2;
    --brand-ink: #1f8fb0;
    --brand-mark: #1d4d58;
    --contact-ink: #1d4d58;
    --tagline-ink: #5b8590;
  }
  * { box-sizing: border-box; margin: 0; padding: 0; }
  html, body {
    width: 1063px;
    height: 1200px;
    overflow: hidden;
    background: var(--backdrop);
  }
  .letterhead {
    position: relative;
    width: 1063px;
    height: 1200px;
    background: var(--paper);
    font-family: "Dosis", sans-serif;
  }
  .letterhead__rule {
    position: absolute;
    left: 0;
    width: 100%;
    height: 1px;
    background: var(--rule-soft);
  }
  .letterhead__rule--top { top: 64px; }
  .letterhead__rule--bottom { top: 236px; background: var(--rule); }
  .letterhead__header {
    position: absolute;
    top: 65px;
    left: 0;
    width: 100%;
    height: 171px;
  }
  .brand {
    position: absolute;
    left: 42px;
    top: 20px;
    width: 230px;
    text-align: center;
  }
  .brand__mark {
    display: block;
    margin: 0 auto 10px;
  }
  .brand__name {
    display: block;
    font-size: 17px;
    font-weight: 500;
    letter-spacing: 2px;
    text-transform: uppercase;
    color: var(--brand-ink);
    line-height: 1.1;
  }
  .brand__tagline {
    display: block;
    margin-top: 6px;
    font-size: 8px;
    font-weight: 500;
    letter-spacing: 2px;
    text-transform: uppercase;
    color: var(--tagline-ink);
  }
  .contact {
    position: absolute;
    right: 36px;
    top: 22px;
    list-style: none;
    color: var(--contact-ink);
    font-size: 15px;
    font-weight: 400;
    line-height: 20px;
  }
  .contact__item {
    display: flex;
    align-items: flex-start;
    gap: 10px;
    margin-bottom: 2px;
  }
  .contact__icon {
    flex: 0 0 14px;
    margin-top: 3px;
  }
</style>
</head>
<body>
  <main class="letterhead">
    <div class="letterhead__rule letterhead__rule--top"></div>
    <header class="letterhead__header">
      <div class="brand">
        <svg class="brand__mark" width="60" height="60" viewBox="0 0 60 60" aria-hidden="true">
          <circle cx="30" cy="30" r="28" fill="none" stroke="#1d4d58" stroke-width="2"/>
        </svg>
        <span class="brand__name">Gold Lantern Pictures</span>
        <span class="brand__tagline">A media entertainment company</span>
      </div>
      <ul class="contact">
        <li class="contact__item">
          <svg class="contact__icon" width="14" height="16" viewBox="0 0 14 16" aria-hidden="true">
            <path d="M7 1a5 5 0 0 1 5 5c0 4-5 9-5 9S2 10 2 6a5 5 0 0 1 5-5z" fill="#1d4d58"/>
            <circle cx="7" cy="6" r="2" fill="#ffffff"/>
          </svg>
          <span>Ridgeway Studio Park<br>2850 Halverson Street<br>Tower Annex, 4th Floor<br>Manhattan Beach, CA 90412</span>
        </li>
        <li class="contact__item">
          <svg class="contact__icon" width="14" height="14" viewBox="0 0 14 14" aria-hidden="true">
            <path d="M3 1.5h2.5l1 3-1.6 1.2a7 7 0 0 0 3.4 3.4L9.5 7.5l3 1V11a1.5 1.5 0 0 1-1.5 1.5A10 10 0 0 1 1.5 3 1.5 1.5 0 0 1 3 1.5z" fill="#1d4d58"/>
          </svg>
          <span>310-555-0148</span>
        </li>
        <li class="contact__item">
          <svg class="contact__icon" width="14" height="14" viewBox="0 0 14 14" aria-hidden="true">
            <rect x="1" y="3" width="12" height="8" rx="1" fill="none" stroke="#1d4d58" stroke-width="1.4"/>
            <path d="M1.5 3.5 7 8l5.5-4.5" fill="none" stroke="#1d4d58" stroke-width="1.4"/>
          </svg>
          <span>info@goldlanternpicturesco.example</span>
        </li>
        <li class="contact__item">
          <svg class="contact__icon" width="14" height="14" viewBox="0 0 14 14" aria-hidden="true">
            <circle cx="7" cy="7" r="5.5" fill="none" stroke="#1d4d58" stroke-width="1.3"/>
            <ellipse cx="7" cy="7" rx="2.4" ry="5.5" fill="none" stroke="#1d4d58" stroke-width="1.1"/>
            <path d="M1.5 7h11" stroke="#1d4d58" stroke-width="1.1"/>
          </svg>
          <span>www.goldlanternpicturesco.example</span>
        </li>
      </ul>
    </header>
    <div class="letterhead__rule letterhead__rule--bottom"></div>
  </main>
</body>
</html>
```